We are a doctors medical practice
I need the business card to be eye catching and memorable,
to reflect professionalism, yet also warmth and care

the numbers need to be easy to see, for the elderly

and the logo also in a location that is large enough to see and be eye catching

Back of card:
opening hours:
Mon- Fri 8.30am to 6pm
Sat 9am to 4pm

rows for appontments, date and time
Updates

HiĀ 

Modification to company name

BRAMBLEWOOD HOME HEALTH MEDICAL PRACTICE

Thanks
Clara

Reason: I am look for a unique design that also fulfils the design brief

I have attempted to post a .eps and .ai file of the logo

Target Market(s)

needs to appeal to the majority, mainly adults

Industry/Entity Type

Medical

Contact Information for Business Card

company name: Bramblewood Home Health Medical Practice
Name: Dr Clara Ostrowski-Vey
Qualifications: MBBS, Bsci(med), FRACGP, DCH, SH&FPA, Dip Derm
Address: Shop 3/41-43 Calder Rd, Brookvale 2371
Ph: 02 9418 3052
Fax: 02 9436 8120

Requirements
Nice to have
• I like balance
gold/ silver incorporated, as well as the other colours in the logo- but not limited to these colours
a "medical" feel
Should not have
• dark or strong colours

```html
<!DOCTYPE html>
<html lang="en">
<head>
<meta charset="utf-8">
<title>Bramblewood Home Health Medical Practice – Business Card</title>
<link rel="stylesheet" href="https://fonts.googleapis.com/css2?family=Arimo:wght@400;700&family=Crimson+Text:wght@400;700&display=swap">
<style>
  :root {
    --page-bg: #e4e5e6;
    --navy: #0f4c97;
    --blue: #1c6fbd;
    --green: #69b844;
    --green-deep: #4f9e33;
    --white: #ffffff;
    --card-w: 680px;
    --card-h: 412px;
  }
  * { box-sizing: border-box; margin: 0; padding: 0; }
  html, body {
    width: 753px;
    height: 1200px;
    overflow: hidden;
    background: var(--page-bg);
  }
  .business-card {
    position: absolute;
    left: 36px;
    top: 394px;
    width: var(--card-w);
    height: var(--card-h);
    overflow: hidden;
    background: var(--white);
    box-shadow: 0 4px 14px rgba(0,0,0,0.18);
  }
  .card-background {
    position: absolute;
    inset: 0;
    width: 100%;
    height: 100%;
  }
  .practice-name {
    position: absolute;
    left: 40px;
    top: 96px;
    width: 220px;
    height: 220px;
    display: flex;
    align-items: center;
    justify-content: center;
    text-align: center;
    font-family: "Arimo", Arial, sans-serif;
    font-weight: 700;
    font-size: 17px;
    line-height: 1.3;
    letter-spacing: 0.5px;
    color: var(--navy);
    padding: 0 28px;
  }
  .doctor-details {
    position: absolute;
    right: 30px;
    top: 28px;
  }
  .doctor-name {
    font-family: "Crimson Text", Georgia, serif;
    font-weight: 700;
    font-size: 27px;
    color: var(--navy);
    line-height: 1.1;
  }
  .qualifications {
    margin-left: 26px;
    margin-top: 4px;
    font-family: "Crimson Text", Georgia, serif;
    font-size: 18px;
    line-height: 1.2;
    color: var(--green-deep);
  }
  .contact-list {
    position: absolute;
    left: 300px;
    right: 0;
    top: 186px;
    list-style: none;
  }
  .contact-bar {
    position: relative;
    height: 32px;
    margin-bottom: 9px;
    border-radius: 16px 0 0 16px;
    background: var(--green);
    color: var(--white);
    font-family: "Arimo", Arial, sans-serif;
    font-size: 15px;
    line-height: 32px;
    text-align: right;
    padding-right: 14px;
    padding-left: 36px;
    white-space: nowrap;
  }
  .contact-bar--fax { background: var(--blue); }
  .contact-icon {
    position: absolute;
    left: 4px;
    top: 4px;
    width: 24px;
    height: 24px;
    border-radius: 50%;
    background: var(--white);
    display: flex;
    align-items: center;
    justify-content: center;
  }
  .contact-icon svg { width: 15px; height: 15px; }
</style>
</head>
<body>
  <article class="business-card">
    <svg class="card-background" viewBox="0 0 680 412" aria-hidden="true">
      <rect class="left-panel" width="680" height="412" fill="var(--navy)"/>
      <circle class="green-sweep" cx="560" cy="206" r="318" fill="var(--green)"/>
      <circle class="white-field" cx="580" cy="206" r="292" fill="var(--white)"/>
      <circle class="logo-ring" cx="150" cy="206" r="118" fill="var(--green)"/>
      <circle class="logo-disc" cx="150" cy="206" r="108" fill="var(--white)"/>
    </svg>

    <div class="practice-name">BRAMBLEWOOD HOME HEALTH MEDICAL PRACTICE</div>

    <header class="doctor-details">
      <h1 class="doctor-name">Dr Clara Ostrowski-Vey</h1>
      <p class="qualifications">MBBS, Bsci(med), FRACGP,<br>DCH, SH&amp;FPA, Dip Derm</p>
    </header>

    <ul class="contact-list">
      <li class="contact-bar contact-bar--phone">
        <span class="contact-icon">
          <svg viewBox="0 0 16 16" aria-hidden="true"><path d="M4 1.5l2 3-1.3 1.5a8 8 0 0 0 5.3 5.3L11.5 10l3 2-1 2.5C7 14.5 1.5 9 1.5 2.5z" fill="var(--green)"/></svg>
        </span>
        Ph: 02 9418 3052
      </li>
      <li class="contact-bar contact-bar--fax">
        <span class="contact-icon">
          <svg viewBox="0 0 16 16" aria-hidden="true"><rect x="4" y="1.5" width="8" height="4" fill="none" stroke="var(--blue)" stroke-width="1.4"/><rect x="1.5" y="5.5" width="13" height="6" rx="1" fill="var(--blue)"/><rect x="4" y="9.5" width="8" height="5" fill="var(--white)" stroke="var(--blue)" stroke-width="1.4"/></svg>
        </span>
        Fax: 02 9436 8120
      </li>
      <li class="contact-bar contact-bar--address">
        <span class="contact-icon">
          <svg viewBox="0 0 16 16" aria-hidden="true"><path d="M8 1.5L1 8h2v6.5h4v-4h2v4h4V8h2z" fill="var(--green)"/></svg>
        </span>
        Shop 3/41-43 Calder Rd, Brookvale 2371
      </li>
    </ul>
  </article>
</body>
</html>
```